skyMARLOW Helicopter Tour WordPress Website Design

SkyMARLOW (skymarlow-tours.example) is a premium helicopter tour company offering scenic flights in two Florida cities: Tampa and Sarasota. We are seeking a full Wordpress website redesign that is modern, upbeat, inviting, and highly conversion‑focused. The new site should feel energetic and trustworthy, reflect the excitement of helicopter sightseeing, and maintain our recognizable SkyMARLOW color palette—while updating the overall look to feel fresh, clean, and current.
The website must be SEO‑friendly, mobile‑optimized, and easy to navigate. It should highlight our 5‑star customer reviews, showcase our tours clearly, and integrate seamlessly with TicketPine for instant online booking. The design should support a premium aviation experience while remaining friendly and accessible to tourists, families, couples, and adventure seekers.

These elements are essential and must be included in the design:

Brand & UX:
- Modern, upbeat, inviting design
- SEO‑friendly structure and layout
- Easy navigation and clear user flow
- Light grey “SM” background logo watermark (as used on current site)
- Clean, aviation‑inspired typography and layout

Conversion Features:
- Instant booking above the fold (TicketPine integration)
- Live plain review marker Reviews carousel
- Tour comparison table (duration, route, price, etc.)
- FAQ expandable section
- Gift Cards page (highlighted as a major offering)
- What to Expect timeline (Arrive → Check‑In → Safety Briefing → Flight → Photos)
- Weather transparency widget (clear messaging about weather‑dependent flights

Content Structure:
- Separate pages for Tampa, Sarasota, and Gender Reveal Flights
- Pilot/Team profiles with short bios
- Highlighted features:
- Doors‑Off option
- Sunset flights
- Romantic packages
- Champagne add‑ons

Colors:
Use the existing SkyMARLOW palette as the foundation, but modernize it.
- Background: Clean with the light grey “SM” watermark integrated tastefully.
The overall color direction should feel bright, premium, energetic, and trustworthy

Target Market(s)

Tourists visiting Tampa or Sarasota, Families looking for memorable activities, Couples seeking romantic experiences (sunset flights, proposals, anniversaries), Adventure seekers and content creators, Locals celebrating birthdays, holidays, or special occasions, Gender reveal clients looking for a unique aerial reveal experience

Industry/Entity Type

Travel & Tourism / Aviation / Helicopter Tours / Experience‑based Activities

Requirements
Must have
• These elements are essential and must be included in the design: Brand & UX - Modern, upbeat, inviting design / SEO‑friendly structure and layout / Easy navigation and clear user flow / Light grey “SM” background logo watermark (as used on current site) / Clean, aviation‑inspired typography and layout
Nice to have
• Interactive route map showing flight paths / Subtle motion or parallax effects in hero sections / Animated icons or micro‑interactions / Social media integration (Instagram grid, TikTok clips) / Sticky mobile booking bar / Video header or short aerial footage loop / Subtle aviation‑themed graphic elements (rotor blur, sky gradients, etc.
Should not have
• No dark, heavy, or overly moody themes / No outdated fonts or overly playful typography / No cluttered layouts or excessive text blocks / No stocky, generic tourism imagery / No slow‑loading animations or heavy effects that hurt SEO

```html
<!DOCTYPE html>
<html lang="en">
<head>
<meta charset="utf-8">
<title>SkyMARLOW – Helicopter Tours in Tampa &amp; Sarasota</title>
<link href="https://fonts.googleapis.com/css2?family=Prata&family=Urbanist:wght@400;500;600;700&display=swap" rel="stylesheet">
<style>
:root{
  --orange:#F7941D;
  --orange-deep:#EE6A0E;
  --blue:#2176C8;
  --blue-dark:#1A63AD;
  --ink:#222831;
  --muted:#5d6570;
  --line:#e3e6ea;
  --soft-blue:#EEF5FC;
  --footer:#333333;
  --white:#ffffff;
  --green:#3BA55C;
}
*{box-sizing:border-box;margin:0;padding:0}
html,body{width:1200px;height:4040px;overflow:hidden;background:#fff}
body{font-family:"Urbanist",sans-serif;color:var(--ink);position:relative}
.abs{position:absolute}
.serif{font-family:"Prata",serif;font-weight:400}
.btn{position:absolute;display:flex;align-items:center;justify-content:center;gap:7px;border-radius:30px;font-weight:700;font-size:12.5px;color:#fff;letter-spacing:.2px}
.btn-orange{background:linear-gradient(90deg,var(--orange),var(--orange-deep))}
.btn-blue{background:var(--blue)}
.btn-ghost{border:2px solid #fff}
/* hero */
.hero{left:0;top:0;width:1200px;height:722px;background:linear-gradient(180deg,#3a4a5e 0%,#2a3a50 35%,#4a5a6a 70%,#6b7785 100%)}
.hero-shade{left:0;top:0;width:1200px;height:722px;background:linear-gradient(90deg,rgba(15,25,40,.55),rgba(15,25,40,.15))}
.nav-logo{left:141px;top:30px;color:#fff;font-weight:700;font-size:20px;letter-spacing:1px;display:flex;align-items:center;gap:8px}
.nav-logo i{width:12px;height:12px;border-radius:50%;background:var(--orange);display:block}
.nav{left:343px;top:38px;color:#fff;font-size:12.5px;font-weight:500}
.nav span{position:absolute;white-space:nowrap}
.hero-stars{left:163px;top:198px;color:#fff;font-size:13px;display:flex;align-items:center;gap:6px}
.stars{color:var(--orange);letter-spacing:1px;font-size:16px}
.hero-title{left:143px;top:232px;width:560px;color:#fff;font-size:47px;line-height:55px}
.hero-sub{left:143px;top:354px;width:460px;color:#fff;font-size:15px;line-height:22px}
.stat{position:absolute;top:505px;color:#fff}
.stat b{display:block;font-size:30px;font-weight:600;line-height:36px}
.stat small{font-size:13px}
/* booking */
.booking{left:715px;top:129px;width:342px;height:494px;background:#fff;border-radius:14px;box-shadow:0 10px 30px rgba(0,0,0,.15)}
.booking h2{position:absolute;left:0;top:30px;width:100%;text-align:center;font-size:22px}
.booking .sub{position:absolute;top:63px;width:100%;text-align:center;font-size:12px;color:var(--muted)}
.fld-label{position:absolute;left:24px;font-size:12px;font-weight:600;color:#333}
.fld{position:absolute;border:1px solid #dcdfe3;border-radius:6px;height:39px;font-size:12px;color:#777;display:flex;align-items:center;padding:0 16px;justify-content:space-between}
.check{position:absolute;left:24px;font-size:12px;color:#666;display:flex;align-items:center;gap:8px}
.check i{width:13px;height:13px;border:1px solid #bbb;border-radius:2px;display:block}
/* weather */
.weather{left:212px;top:670px;width:776px;height:103px;background:#fff;border-radius:8px;box-shadow:0 8px 28px rgba(0,0,0,.1)}
.w-ico{position:absolute;top:27px;width:50px;height:50px;border-radius:50%;background:var(--soft-blue);display:flex;align-items:center;justify-content:center}
.w-txt{position:absolute;top:34px;font-size:12.5px;color:#777;line-height:18px}
.w-txt b{color:var(--ink);font-weight:600}
/* section titles */
.sec-title{position:absolute;left:0;width:1200px;text-align:center;font-size:35px;color:var(--blue);letter-spacing:.5px}
.sec-sub{position:absolute;left:0;width:1200px;text-align:center;font-size:13px;color:#333}
.mark{position:absolute;font-family:"Prata",serif;font-size:78px;color:rgba(150,158,168,.18);letter-spacing:-4px}
/* tour cards */
.card{position:absolute;top:954px;width:291px;height:455px;border:1px solid var(--line);border-radius:12px;overflow:hidden;background:#fff}
.card-img{height:188px;background:linear-gradient(160deg,#7aa9cf,#3f6f96 55%,#c7b79e)}
.pill{position:absolute;top:15px;height:24px;padding:0 12px;border-radius:14px;font-size:11px;color:#fff;display:flex;align-items:center}
.card h3{position:absolute;left:21px;top:206px;font-size:17px}
.card p{position:absolute;left:21px;top:234px;width:250px;font-size:12px;line-height:19px;color:#444}
.feat{position:absolute;left:21px;font-size:12.5px;color:#333;display:flex;align-items:center;gap:9px}
.arrow-c{position:absolute;top:1115px;width:55px;height:55px;border-radius:50%;border:1px solid #ccd;display:flex;align-items:center;justify-content:center;background:#fff}
/* compare */
.compare{left:0;top:1501px;width:1200px;height:606px;background:linear-gradient(135deg,#2b80cf,#1e6fbd 60%,#2a7acb)}
.tbl{position:absolute;left:141px;top:1680px;width:917px}
.tbl-head{height:53px;background:linear-gradient(90deg,var(--orange),var(--orange-deep));border-radius:6px 6px 0 0;color:#fff;font-size:18px;position:relative}
.tbl-row{height:56.5px;position:relative;color:#fff;font-size:14px}
.tbl-row:nth-child(even){background:#2a83d2}
.tbl-row:nth-child(odd){background:#2278c8}
.tbl .c{position:absolute;top:50%;transform:translateY(-50%)}
.tbl-btn{position:absolute;left:772px;top:12px;width:118px;height:33px;border:1.5px solid #fff;border-radius:18px;font-size:11px;font-weight:700;display:flex;align-items:center;justify-content:center;gap:6px}
/* expect */
.step{position:absolute;width:220px;text-align:center}
.step .circ{width:113px;height:113px;border-radius:50%;background:#fff;box-shadow:0 6px 24px rgba(0,0,0,.09);margin:0 auto;display:flex;align-items:center;justify-content:center}
.step .num{width:30px;height:30px;border-radius:50%;background:var(--orange);color:#fff;font-size:12px;margin:-14px auto 0;display:flex;align-items:center;justify-content:center;position:relative}
.step h4{font-family:"Prata",serif;font-weight:400;font-size:15px;margin-top:8px}
.step p{font-size:11px;line-height:20px;color:#444;margin:8px auto 0;width:180px}
/* reviews */
.reviews{left:0;top:2648px;width:1200px;height:494px;background:var(--soft-blue)}
.rev{position:absolute;top:2828px;width:251px;height:225px;background:#fff;border-radius:6px;box-shadow:0 4px 14px rgba(0,0,0,.04)}
.rev .av{position:absolute;left:17px;top:19px;width:28px;height:28px;border-radius:50%;color:#fff;font-size:12px;display:flex;align-items:center;justify-content:center}
.rev .nm{position:absolute;left:56px;top:17px;font-size:13px;font-weight:600}
.rev .tm{position:absolute;left:56px;top:36px;font-size:11px;color:#888}
.rev .gm{position:absolute;right:18px;top:20px;width:24px;height:24px;border-radius:50%;border:3px solid #4a86e0}
.rev .st{position:absolute;left:17px;top:56px}
.rev p{position:absolute;left:17px;top:98px;width:220px;font-size:12.5px;line-height:20.5px;color:#666}
/* faq */
.faq{position:absolute;width:444px;background:#fff;border-radius:6px;box-shadow:0 4px 18px rgba(0,0,0,.08);font-size:12.5px;font-weight:600}
.faq .q{position:absolute;left:18px;top:19px}
.faq .tg{position:absolute;right:18px;top:17px;width:20px;height:20px;border-radius:50%;background:var(--blue);display:flex;align-items:center;justify-content:center}
/* footer */
.footer{left:0;top:3663px;width:1200px;height:377px;background:var(--footer);color:#fff}
.f-h{position:absolute;top:69px;font-family:"Prata",serif;font-size:15px;border-left:2px solid var(--orange);padding-left:9px}
.f-t{position:absolute;font-size:12px;line-height:24px;color:#e8e8e8}
.soc{position:absolute;top:218px;width:24px;height:24px;border-radius:50%;border:1px solid #ddd}
</style>
</head>
<body>

<!-- HERO -->
<section class="abs hero" role="img" aria-label="Aerial night view of the Tampa city skyline and waterfront"></section>
<div class="abs hero-shade"></div>
<div class="abs nav-logo"><i></i>SKYMARLOW</div>
<nav class="abs nav">
  <span style="left:0">TOURS</span><span style="left:62px">TAMPA</span><span style="left:124px">SARASOTA</span><span style="left:211px">GENDER REVEAL</span><span style="left:330px">GIFT CARDS</span><span style="left:426px">ABOUT</span><span style="left:489px">CONTACT</span>
</nav>
<div class="btn btn-orange" style="left:914px;top:28px;width:143px;height:43px">
  <svg width="13" height="13" viewBox="0 0 14 14" fill="none" stroke="#fff" stroke-width="1.6"><rect x="1.5" y="2.5" width="11" height="10" rx="1.5"/><path d="M1.5 6h11M4.5 1v3M9.5 1v3"/></svg>BOOK NOW</div>

<div class="abs hero-stars"><span class="stars">★★★★★</span>500+ 5-Star Reviews</div>
<h1 class="abs serif hero-title">Experience Florida<br>From Above</h1>
<p class="abs hero-sub">Premium Helicopter Tours in Tampa &amp; Sarasota. Unforgettable aerial adventures for every occasion.</p>
<div class="btn btn-orange" style="left:141px;top:427px;width:190px;height:40px">
  <svg width="13" height="13" viewBox="0 0 14 14" fill="none" stroke="#fff" stroke-width="1.6"><rect x="1.5" y="2.5" width="11" height="10" rx="1.5"/><path d="M1.5 6h11M4.5 1v3M9.5 1v3"/></svg>BOOK YOUR FLIGHT</div>
<div class="btn btn-ghost" style="left:342px;top:425px;width:143px;height:43px">
  <svg width="13" height="13" viewBox="0 0 14 14" fill="none" stroke="#fff" stroke-width="1.6"><circle cx="7" cy="7" r="5.5"/><path d="M6 4.5 8.5 7 6 9.5"/></svg>VIEW TOURS</div>
<div class="stat" style="left:143px"><b>10K+</b><small>Happy Flyers</small></div>
<div class="stat" style="left:272px"><b>15+</b><small>Years Flying</small></div>
<div class="stat" style="left:395px"><b>100%</b><small>Safety Record</small></div>

<!-- BOOKING -->
<aside class="abs booking">
  <h2 class="serif">BOOK YOUR ADVENTURE</h2>
  <div class="sub">Select your experience and preferred date</div>
  <div class="fld-label" style="top:99px">Location</div>
  <div class="fld" style="left:24px;top:122px;width:295px">Tampa<svg width="9" height="6" viewBox="0 0 9 6"><path d="M1 1l3.5 3.5L8 1" stroke="#666" fill="none"/></svg></div>
  <div class="fld-label" style="top:177px">Tour Type</div>
  <div class="fld" style="left:24px;top:199px;width:295px">Intro Flight (15 min) - $149<svg width="9" height="6" viewBox="0 0 9 6"><path d="M1 1l3.5 3.5L8 1" stroke="#666" fill="none"/></svg></div>
  <div class="fld-label" style="top:254px">Date</div>
  <div class="fld-label" style="top:254px;left:178px">Passengers</div>
  <div class="fld" style="left:24px;top:277px;width:141px">date/dd/yyyy<svg width="12" height="12" viewBox="0 0 14 14" fill="none" stroke="#666" stroke-width="1.3"><rect x="1.5" y="2.5" width="11" height="10" rx="1"/><path d="M1.5 6h11M4.5 1v3M9.5 1v3"/></svg></div>
  <div class="fld" style="left:178px;top:277px;width:141px">1<svg width="9" height="6" viewBox="0 0 9 6"><path d="M1 1l3.5 3.5L8 1" stroke="#666" fill="none"/></svg></div>
  <div class="fld-label" style="top:333px">Add-ons</div>
  <div class="check" style="top:360px"><i></i>Doors-Off Experience (+$50)</div>
  <div class="check" style="top:388px"><i></i>Champagne Package (+$75)</div>
  <div class="btn btn-orange" style="left:24px;top:418px;width:295px;height:43px;font-size:11.5px">CHECK AVAILABILITY</div>
</aside>

<!-- WEATHER -->
<div class="abs weather">
  <div class="w-ico" style="left:47px"><svg width="24" height="24" viewBox="0 0 24 24" fill="none" stroke="var(--blue)" stroke-width="1.8"><circle cx="12" cy="12" r="4.5"/><path d="M12 2v3M12 19v3M2 12h3M19 12h3M4.9 4.9l2.1 2.1M17 17l2.1 2.1M4.9 19.1 7 17M17 7l2.1-2.1"/></svg></div>
  <div class="w-txt" style="left:111px">Today's Weather<br><b>Perfect Flying Conditions</b></div>
  <div class="w-ico" style="left:351px"><svg width="24" height="24" viewBox="0 0 24 24"><path d="M15 3a9 9 0 1 0 6 13A7.5 7.5 0 0 1 15 3z" fill="var(--blue)"/></svg></div>
  <div class="w-txt" style="left:414px">Clear Skies<br><b>78°F</b></div>
  <div class="w-ico" style="left:552px"><svg width="26" height="22" viewBox="0 0 26 22" fill="none" stroke="var(--blue)" stroke-width="1.8"><path d="M3 3h20M13 3v4"/><path d="M6 9h11a4 4 0 0 1 0 8H9a3 3 0 0 1-3-3z" fill="var(--blue)"/><path d="M6 11H1M8 20h12"/></svg></div>
  <div class="w-txt" style="left:615px;color:var(--ink);font-weight:600">Flights Operating<br>Normally</div>
</div>

<!-- POPULAR TOURS -->
<div class="mark" style="left:330px;top:838px">SM</div>
<h2 class="sec-title serif" style="top:862px">MOST POPULAR TOURS</h2>
<p class="sec-sub" style="top:915px">Choose your perfect aerial adventure from our carefully curated tour collection</p>

<div class="arrow-c" style="left:56px"><svg width="8" height="12" viewBox="0 0 8 12"><path d="M6 1 1 6l5 5" stroke="#aaa" fill="none" stroke-width="1.5"/></svg></div>
<div class="arrow-c" style="left:1082px;border-color:var(--blue)"><svg width="8" height="12" viewBox="0 0 8 12"><path d="M2 1l5 5-5 5" stroke="var(--blue)" fill="none" stroke-width="1.5"/></svg></div>

<article class="card" style="left:141px">
  <div class="card-img" role="img" aria-label="Passengers wearing headsets inside a helicopter over the coastline"></div>
  <span class="pill" style="left:21px;background:var(--blue)">15 min</span>
  <span class="pill" style="right:21px;background:var(--orange)">From $149</span>
  <h3 class="serif">Intro Flight</h3>
  <p>Perfect first-time experience with stunning coastline views and city highlights.</p>
  <div class="feat" style="top:288px"><svg width="17" height="17" viewBox="0 0 17 17" fill="none" stroke="var(--green)" stroke-width="1.6"><circle cx="8.5" cy="8.5" r="7.5"/><path d="M5 8.7l2.4 2.4L12 6.2"/></svg>Scenic coastline route</div>
  <div class="feat" style="top:317px"><svg width="17" height="17" viewBox="0 0 17 17" fill="none" stroke="var(--green)" stroke-width="1.6"><circle cx="8.5" cy="8.5" r="7.5"/><path d="M5 8.7l2.4 2.4L12 6.2"/></svg>Up to 3 passengers</div>
  <div class="feat" style="top:346px"><svg width="17" height="17" viewBox="0 0 17 17" fill="none" stroke="var(--green)" stroke-width="1.6"><circle cx="8.5" cy="8.5" r="7.5"/><path d="M5 8.7l2.4 2.4L12 6.2"/></svg>Digital photos included</div>
  <div class="btn btn-blue" style="left:21px;top:383px;width:149px;height:39px">
    <svg width="12" height="12" viewBox="0 0 14 14" fill="none" stroke="#fff" stroke-width="1.6"><rect x="1.5" y="2.5" width="11" height="10" rx="1.5"/><path d="M1.5 6h11M4.5 1v3M9.5 1v3"/></svg>BOOK NOW</div>
</article>

<article class="card" style="left:453px">
  <div class="card-img" role="img" aria-label="Excited passengers with headsets during a city flight" style="background:linear-gradient(160deg,#9aa7b3,#5e6a76 55%,#c9ced3)"></div>
  <span class="pill" style="left:21px;background:var(--blue)">25 min</span>
  <span class="pill" style="right:21px;background:var(--orange)">From $249</span>
  <h3 class="serif">City Explorer</h3>
  <p>Extended tour covering downtown skyline, bridges, beaches, and iconic landmarks</p>
  <div class="feat" style="top:288px"><svg width="17" height="17" viewBox="0 0 17 17" fill="none" stroke="var(--green)" stroke-width="1.6"><circle cx="8.5" cy="8.5" r="7.5"/><path d="M5 8.7l2.4 2.4L12 6.2"/></svg>Full city skyline views</div>
  <div class="feat" style="top:317px"><svg width="17" height="17" viewBox="0 0 17 17" fill="none" stroke="var(--green)" stroke-width="1.6"><circle cx="8.5" cy="8.5" r="7.5"/><path d="M5 8.7l2.4 2.4L12 6.2"/></svg>Doors-off option available</div>
  <div class="feat" style="top:346px"><svg width="17" height="17" viewBox="0 0 17 17" fill="none" stroke="var(--green)" stroke-width="1.6"><circle cx="8.5" cy="8.5" r="7.5"/><path d="M5 8.7l2.4 2.4L12 6.2"/></svg>HD video recording</div>
  <div class="btn btn-orange" style="left:21px;top:383px;width:149px;height:39px">
    <svg width="12" height="12" viewBox="0 0 14 14" fill="none" stroke="#fff" stroke-width="1.6"><rect x="1.5" y="2.5" width="11" height="10" rx="1.5"/><path d="M1.5 6h11M4.5 1v3M9.5 1v3"/></svg>BOOK NOW</div>
</article>

<article class="card" style="left:767px">
  <div class="card-img" role="img" aria-label="Couple enjoying a golden hour helicopter flight" style="background:linear-gradient(160deg,#a5b7c6,#6b7f8f 50%,#d9c4a3)"></div>
  <span class="pill" style="left:21px;background:var(--blue)">30 min</span>
  <span class="pill" style="right:21px;background:var(--orange)">From $349</span>
  <h3 class="serif">Sunset Flight</h3>
  <p>Magical golden hour experience with breathtaking sunset views over the Gulf.</p>
  <div class="feat" style="top:288px"><svg width="17" height="17" viewBox="0 0 17 17" fill="none" stroke="var(--green)" stroke-width="1.6"><circle cx="8.5" cy="8.5" r="7.5"/><path d="M5 8.7l2.4 2.4L12 6.2"/></svg>Golden hour timing</div>
  <div class="feat" style="top:317px"><svg width="17" height="17" viewBox="0 0 17 17" fill="none" stroke="var(--green)" stroke-width="1.6"><circle cx="8.5" cy="8.5" r="7.5"/><path d="M5 8.7l2.4 2.4L12 6.2"/></svg>Champagne available</div>
  <div class="feat" style="top:346px"><svg width="17" height="17" viewBox="0 0 17 17" fill="none" stroke="var(--green)" stroke-width="1.6"><circle cx="8.5" cy="8.5" r="7.5"/><path d="M5 8.7l2.4 2.4L12 6.2"/></svg>Premium photo package</div>
  <div class="btn btn-blue" style="left:21px;top:383px;width:149px;height:39px">
    <svg width="12" height="12" viewBox="0 0 14 14" fill="none" stroke="#fff" stroke-width="1.6"><rect x="1.5" y="2.5" width="11" height="10" rx="1.5"/><path d="M1.5 6h11M4.5 1v3M9.5 1v3"/></svg>BOOK NOW</div>
</article>

<!-- COMPARE -->
<section class="abs compare" role="img" aria-label="Soft blue backdrop of a pilot's headset"></section>
<div class="mark" style="left:338px;top:1558px;color:rgba(255,255,255,.16)">SM</div>
<h2 class="sec-title serif" style="top:1582px;color:#fff">COMPARE OUR TOURS</h2>
<p class="sec-sub" style="top:1641px;color:#fff">Find the perfect flight for your adventure</p>

<div class="tbl">
  <div class="tbl-head serif"><span class="c" style="left:33px">Tour</span><span class="c" style="left:217px">Duration</span><span class="c" style="left:342px">Route</span><span class="c" style="left:545px">Doors-Off</span><span class="c" style="left:681px">Price</span></div>
  <div>
    <div class="tbl-row"><span class="c" style="left:33px">Intro Flight</span><span class="c" style="left:217px">15 min</span><span class="c" style="left:342px">Coastline</span><span class="c" style="left:545px">✓</span><span class="c" style="left:681px">$149</span><span class="tbl-btn">▣ BOOK NOW</span></div>
    <div class="tbl-row"><span class="c" style="left:33px">City Explorer</span><span class="c" style="left:217px">25 min</span><span class="c" style="left:342px">Downtown + Coast</span><span class="c" style="left:545px">✓</span><span class="c" style="left:681px">$249</span><span class="tbl-btn" style="background:linear-gradient(90deg,var(--orange),var(--orange-deep));border-color:transparent">▣ BOOK NOW</span></div>
    <div class="tbl-row"><span class="c" style="left:33px">Sunset Flight</span><span class="c" style="left:217px">30 min</span><span class="c" style="left:342px">Gulf + Beaches</span><span class="c" style="left:545px">✓</span><span class="c" style="left:681px">$349</span><span class="tbl-btn">▣ BOOK NOW</span></div>
    <div class="tbl-row"><span class="c" style="left:33px">Deluxe Tour</span><span class="c" style="left:217px">45 min</span><span class="c" style="left:342px">Complete Circuit</span><span class="c" style="left:545px">✓</span><span class="c" style="left:681px">$449</span><span class="tbl-btn">▣ BOOK NOW</span></div>
    <div class="tbl-row"><span class="c" style="left:33px">Romantic Package</span><span class="c" style="left:217px">45 min</span><span class="c" style="left:342px">Sunset + Champagne</span><span class="c" style="left:545px">✓</span><span class="c" style="left:681px">$549</span><span class="tbl-btn">▣ BOOK NOW</span></div>
  </div>
</div>

<!-- WHAT TO EXPECT -->
<div class="mark" style="left:370px;top:2164px">SM</div>
<h2 class="sec-title serif" style="top:2188px">WHAT TO EXPECT</h2>
<p class="sec-sub" style="top:2242px">From arrival to takeoff, here's how your aerial adventure unfolds</p>
<svg class="abs" style="left:0;top:2300px" width="1200" height="120" viewBox="0 0 1200 120" fill="none" stroke="#c9ced6" stroke-width="1" stroke-dasharray="3 4">
  <path d="M280 70 Q330 90 360 85"/><path d="M470 70 Q520 30 545 38"/><path d="M660 70 Q700 100 730 85"/><path d="M845 70 Q890 35 920 38"/>
</svg>
<div class="step" style="left:113px;top:2284px">
  <div class="circ"><svg width="50" height="40" viewBox="0 0 50 40"><path d="M8 18l5-11h24l5 11h3v16h-6v4h-5v-4H16v4h-5v-4H5V18z" fill="var(--blue)"/><rect x="14" y="10" width="22" height="8" fill="#fff"/><circle cx="12" cy="25" r="3" fill="#fff"/><circle cx="38" cy="25" r="3" fill="#fff"/></svg></div>
  <div class="num">01</div><h4>Arrive</h4>
  <p>Arrive at our helipad 15 minutes before your scheduled flight. Free parking available.</p>
</div>
<div class="step" style="left:303px;top:2320px">
  <div class="circ"><svg width="46" height="46" viewBox="0 0 46 46"><rect x="6" y="3" width="28" height="38" rx="3" fill="var(--blue)"/><path d="M11 12h4M19 12h10M11 20h4M19 20h10M11 28h4M19 28h6" stroke="#fff" stroke-width="2.4"/><circle cx="34" cy="33" r="9" fill="var(--blue)" stroke="#fff" stroke-width="2"/><path d="M30 33l3 3 5-6" stroke="#fff" stroke-width="2" fill="none"/></svg></div>
  <div class="num">02</div><h4>Check-In</h4>
  <p>Quick and easy check-in process. Our friendly team will verify your booking and answer any questions.</p>
</div>
<div class="step" style="left:491px;top:2284px">
  <div class="circ"><svg width="42" height="46" viewBox="0 0 42 46"><path d="M21 2 38 8v13c0 11-7 19-17 23C11 40 4 32 4 21V8z" fill="var(--blue)"/><path d="M21 8l11 4v9c0 8-5 14-11 17-6-3-11-9-11-17v-9z" fill="#fff"/><path d="M15 22l5 5 8-9" stroke="var(--blue)" stroke-width="3" fill="none"/></svg></div>
  <div class="num">03</div><h4>Safety Briefing</h4>
  <p>Your pilot will provide a comprehensive safety briefing and explain helicopter operations.</p>
</div>
<div class="step" style="left:677px;top:2320px">
  <div class="circ"><svg width="46" height="46" viewBox="0 0 46 46"><circle cx="23" cy="23" r="20" fill="var(--blue)"/><circle cx="23" cy="23" r="15" fill="#fff"/><path d="M23 12v11l7 5" stroke="var(--blue)" stroke-width="2.6" fill="none"/></svg></div>
  <div class="num">04</div><h4>Flight Time!</h4>
  <p>Lift off and enjoy breathtaking aerial views of Florida's most stunning landscapes!</p>
</div>
<div class="step" style="left:866px;top:2284px">
  <div class="circ"><svg width="50" height="40" viewBox="0 0 50 40"><path d="M4 10h10l4-6h14l4 6h10v27H4z" fill="var(--blue)"/><circle cx="25" cy="22" r="10" fill="#fff"/><circle cx="25" cy="22" r="6" fill="var(--blue)"/><rect x="39" y="13" width="4" height="3" fill="#fff"/></svg></div>
  <div class="num">05</div><h4>Photos &amp; Memories</h4>
  <p>Receive your complimentary photos and video to share your amazing experience!</p>
</div>

<!-- REVIEWS -->
<section class="abs reviews"></section>
<div class="mark" style="left:362px;top:2725px">SM</div>
<h2 class="sec-title serif" style="top:2749px">WHAT OUR GUESTS SAY</h2>
<div class="abs" style="left:141px;top:2858px;width:223px;text-align:center">
  <div style="font-size:22px;font-weight:600;letter-spacing:.5px">EXCELLENT</div>
  <div style="margin-top:8px;font-size:19px;color:var(--orange);font-weight:600">4.5 <span class="stars" style="font-size:20px">★★★★★</span></div>
  <div style="margin-top:6px;font-size:14px;color:#444">Based on 225 reviews</div>
</div>
<div class="btn btn-blue" style="left:141px;top:2977px;width:106px;height:28px;border-radius:3px;font-size:11px;font-weight:600">See All Reviews</div>
<div class="btn btn-blue" style="left:258px;top:2977px;width:106px;height:28px;border-radius:3px;font-size:11px;font-weight:600">Review Us <i style="width:10px;height:10px;border-radius:50%;border:2px solid #fff;display:block"></i></div>
<svg class="abs" style="left:364px;top:2934px" width="10" height="14" viewBox="0 0 10 14"><path d="M8 1 2 7l6 6" stroke="#555" fill="none" stroke-width="1.6"/></svg>

<div class="rev" style="left:389px">
  <div class="av" style="background:#b58a6a">M</div><div class="nm">Maya R</div><div class="tm">1 week ago</div><i class="gm"></i>
  <div class="st stars" style="font-size:18px">★★★★★</div>
  <p>Great experience for a first timer! Marco was a great pilot and tour guide. Accommodated our schedule changes and easy to work with. Highly recommend!</p>
</div>
<div class="rev" style="left:662px">
  <div class="av" style="background:#3f51b5">L</div><div class="nm">Leo Tanaka</div><div class="tm">2 weeks ago</div><i class="gm"></i>
  <div class="st stars" style="font-size:18px">★★★★★</div>
  <p>Great experience! Marco is a terrific pilot and very friendly!</p>
</div>
<div class="rev" style="left:935px">
  <div class="av" style="background:#78909c">DJ</div><div class="nm">DJ Carter</div><div class="tm">1 week ago</div><i class="gm"></i>
  <div class="st stars" style="font-size:18px">★★★★★</div>
  <p>Amazing experience. Marco was our pilot and he was awesome. Just great vibes.</p>
</div>
<svg class="abs" style="left:722px;top:3078px" width="120" height="18" viewBox="0 0 120 18">
  <path d="M30 9H2M8 3 2 9l6 6" stroke="#aaa" fill="none" stroke-width="1.5"/>
  <circle cx="38" cy="9" r="2.2" fill="#bbb"/><circle cx="52" cy="9" r="2.6" fill="var(--orange)"/><circle cx="66" cy="9" r="2.2" fill="#bbb"/><circle cx="80" cy="9" r="2.2" fill="#bbb"/>
  <path d="M90 9h28M112 3l6 6-6 6" stroke="var(--orange)" fill="none" stroke-width="1.5"/>
</svg>

<!-- FAQ -->
<div class="mark" style="left:250px;top:3202px">SM</div>
<h2 class="sec-title serif" style="top:3226px">FREQUENTLY ASKED QUESTIONS</h2>
<p class="sec-sub" style="top:3287px">Everything you need to know before your flight</p>
<div class="faq" style="left:141px;top:3327px;height:53px"><span class="q">Lorem Ipsum is simply dummy text?</span><span class="tg"><svg width="9" height="6" viewBox="0 0 9 6"><path d="M1 1l3.5 3.5L8 1" stroke="#fff" fill="none" stroke-width="1.5"/></svg></span></div>
<div class="faq" style="left:141px;top:3391px;height:53px"><span class="q">Standard dummy text ever since the 1500s when?</span><span class="tg"><svg width="9" height="6" viewBox="0 0 9 6"><path d="M1 1l3.5 3.5L8 1" stroke="#fff" fill="none" stroke-width="1.5"/></svg></span></div>
<div class="faq" style="left:141px;top:3454px;height:53px"><span class="q">Printer took a galley of type and scrambled?</span><span class="tg"><svg width="9" height="6" viewBox="0 0 9 6"><path d="M1 1l3.5 3.5L8 1" stroke="#fff" fill="none" stroke-width="1.5"/></svg></span></div>
<div class="faq" style="left:141px;top:3517px;height:53px"><span class="q">Lectronic typesetting remaining unchanged?</span><span class="tg"><svg width="9" height="6" viewBox="0 0 9 6"><path d="M1 1l3.5 3.5L8 1" stroke="#fff" fill="none" stroke-width="1.5"/></svg></span></div>
<div class="faq" style="left:615px;top:3327px;height:176px"><span class="q">Lectronic typesetting remaining unchanged?</span><span class="tg" style="background:var(--orange)"><svg width="9" height="6" viewBox="0 0 9 6"><path d="M1 5l3.5-3.5L8 5" stroke="#fff" fill="none" stroke-width="1.5"/></svg></span>
  <p style="position:absolute;left:18px;top:66px;width:400px;font-weight:400;font-size:12px;line-height:21px;color:#444">Lorem ipsum dolor sit amet, consectetuer adipiscing elit, sed diam nonummy nibh euismod tincidunt ut laoreet dolore magna aliquam erat volutpat. Ut wisi enim ad minim veniam, quis nostrud exerci tation ullamcorper suscipit.</p></div>
<div class="faq" style="left:615px;top:3517px;height:53px"><span class="q">Standard dummy text ever since the 1500s when?</span><span class="tg"><svg width="9" height="6" viewBox="0 0 9 6"><path d="M1 1l3.5 3.5L8 1" stroke="#fff" fill="none" stroke-width="1.5"/></svg></span></div>

<!-- FOOTER -->
<footer class="abs footer">
  <div class="f-h" style="left:143px">ABOUT SKYMARLOW</div>
  <p class="f-t" style="left:143px;top:108px;width:210px">Ut wisi enim ad minim veniam, quis nostrud exerci tation ullamcorper suscipit lobortis nisl ut aliquip ex ea commodo consequat.</p>
  <span class="soc" style="left:143px;background:var(--orange);border-color:var(--orange)"></span>
  <span class="soc" style="left:179px"></span><span class="soc" style="left:215px"></span><span class="soc" style="left:251px"></span>

  <div class="f-h" style="left:424px">CONTACT DETAILS</div>
  <svg class="abs" style="left:426px;top:115px" width="12" height="12" viewBox="0 0 12 12"><path d="M2 1h3l1 3-2 1a7 7 0 0 0 3 3l1-2 3 1v3c-6 0-9-3-9-9z" fill="#fff"/></svg>
  <p class="f-t" style="left:448px;top:106px;line-height:19px"><b style="font-weight:600">Phone</b><br>(844) 555-0142</p>
  <svg class="abs" style="left:426px;top:161px" width="12" height="10" viewBox="0 0 12 10"><rect width="12" height="10" rx="1" fill="#fff"/><path d="M0 1l6 4 6-4" stroke="#333" fill="none"/></svg>
  <p class="f-t" style="left:448px;top:153px;line-height:19px"><b style="font-weight:600">Email</b><br>info@skymarlow-tours.example</p>
  <svg class="abs" style="left:425px;top:206px" width="13" height="13" viewBox="0 0 13 13" fill="none" stroke="#fff" stroke-width="1.4"><circle cx="6.5" cy="6.5" r="5.5"/><path d="M6.5 3.5v3l2 1.5"/></svg>
  <p class="f-t" style="left:448px;top:198px;line-height:19px"><b style="font-weight:600">Opening Hours</b><br>Mon-Sat 9:00am - 5:30pm<br>Sun 10:00am - 3:00pm</p>

  <div class="f-h" style="left:681px">QUICK LINKS</div>
  <p class="f-t" style="left:681px;top:106px">• Tours<br>• Tampa<br>• Sarasota<br>• Gender Reveal<br>• Gift Cards<br>• About<br>• Contact</p>

  <div class="abs" style="left:850px;top:150px;width:220px;font-size:26px;font-weight:700;letter-spacing:1px;display:flex;align-items:center;justify-content:center;gap:10px"><i style="width:14px;height:14px;border-radius:50%;background:var(--orange);display:block"></i>SKYMARLOW</div>

  <div class="abs" style="left:141px;top:321px;width:917px;height:1px;background:#555"></div>
  <p class="abs" style="left:0;top:341px;width:1200px;text-align:center;font-size:11.5px;color:#ddd">© 2026 SkyMARLOW. All Rights Reserved.</p>
</footer>

</body>
</html>
```